Professional Business Card for Commercial Cleaning Company

We need a business card that represents our commercial janitorial cleaning company and represent several brands for our company so we do not want to highlight the logo too much. We want something that says we are professional.
Notes:No website or address as we have many locations and many websites and companies under our corporate name of "Brightvale Holdings, LLC" . Every time we hand a customer a business card they have contacted us via another brand we own but we don't want to have 21 business cards so we want to not focus on Brightvale Holdings, LLC too much since people will automatically ask "What is Brightvale Holdings, LLC" Example: Noodle Barn and Wrap Lantern restaurants are owned by "Zest! Brands" is the corporation name. Same principle here. Except we do not advertise at this time that all of our brands are connected. Hope this helps.
Target Market(s)
Commercial Cleaning
Industry/Entity Type
Janitorial Service
Contact Information for Business Card
Milo Jarvis
Business Development
555-382-9047
sales@brightvaleholdingsllc.example
Requirements
Must have
- Logo with contact information, need to be able to easily edit contact info for others in my office.
Nice to have
- Professional Image. Like to see a colorful bold look and a more standard business card look.
Should not have
- Any type of cleaning icons, tools, people or water.

```html
<!DOCTYPE html>
<html lang="en">
<head>
<meta charset="utf-8">
<title>Brightvale Holdings, LLC – Business Card</title>
<link rel="stylesheet" href="https://fonts.googleapis.com/css2?family=Montserrat:wght@700&family=Lato:wght@400&display=swap">
<style>
  :root {
    --navy: #1d3f7a;
    --green: #6aa842;
    --white: #ffffff;
    --grey: #4a4a4a;
    --stage: #e6e7ea;
  }
  * { box-sizing: border-box; margin: 0; padding: 0; }
  html, body { width: 1200px; height: 900px; overflow: hidden; }
  body {
    background: var(--stage);
    display: flex;
    flex-direction: column;
    align-items: center;
    justify-content: center;
    gap: 60px;
    font-family: "Lato", sans-serif;
  }
  .card {
    position: relative;
    width: 600px;
    height: 343px;
    overflow: hidden;
    box-shadow: 0 6px 18px rgba(0,0,0,0.18);
  }
  .brand-name {
    font-family: "Montserrat", sans-serif;
    font-weight: 700;
    letter-spacing: 0.5px;
    white-space: nowrap;
  }

  /* Front */
  .card-front { background: var(--navy); }
  .card-front .brand-name {
    position: absolute;
    left: 50%; top: 50%;
    transform: translate(-50%, -50%);
    color: var(--white);
    font-size: 38px;
  }

  /* Back */
  .card-back { background: var(--white); }
  .card-back .brand-name {
    position: absolute;
    left: 120px; top: 62px;
    color: var(--navy);
    font-size: 32px;
  }
  .contact-list {
    position: absolute;
    right: 28px; top: 118px;
    list-style: none;
    text-align: right;
    color: var(--grey);
    font-size: 14px;
    line-height: 22px;
  }
  .contact-list li { display: flex; align-items: center; justify-content: flex-end; gap: 8px; }
  .contact-icon { width: 12px; height: 12px; fill: var(--green); }
  .edge-mark-navy {
    position: absolute; right: 0; top: 104px;
    width: 14px; height: 30px; background: var(--navy);
  }
  .edge-mark-green {
    position: absolute; left: 0; top: 232px;
    width: 24px; height: 34px; background: var(--green);
  }
  .person {
    position: absolute; left: 36px; top: 228px;
  }
  .person-name {
    font-family: "Montserrat", sans-serif;
    font-weight: 700;
    font-size: 24px;
    color: var(--navy);
    text-transform: uppercase;
    letter-spacing: 0.5px;
    line-height: 26px;
  }
  .person-title { font-size: 14px; color: var(--grey); letter-spacing: 0.5px; }
  .wave-band { position: absolute; left: 0; top: 0; width: 600px; height: 343px; }
</style>
</head>
<body>
  <section class="card card-front" aria-label="Card front">
    <div class="brand-name">Brightvale Holdings, LLC</div>
  </section>

  <section class="card card-back" aria-label="Card back">
    <svg class="wave-band" viewBox="0 0 600 343" aria-hidden="true">
      <path d="M0 343 L0 334 C170 318 360 250 600 128 L600 343 Z" fill="var(--navy)"/>
      <path d="M190 343 C330 292 470 210 600 136 L600 146 C480 220 350 300 232 343 Z"
            fill="var(--green)" stroke="var(--white)" stroke-width="2"/>
    </svg>

    <div class="brand-name">Brightvale Holdings, LLC</div>

    <span class="edge-mark-navy"></span>
    <ul class="contact-list">
      <li>555-382-9047
        <svg class="contact-icon" viewBox="0 0 24 24"><path d="M6.6 10.8a15.1 15.1 0 0 0 6.6 6.6l2.2-2.2a1 1 0 0 1 1-.25 11.4 11.4 0 0 0 3.6.6 1 1 0 0 1 1 1V20a1 1 0 0 1-1 1A17 17 0 0 1 3 4a1 1 0 0 1 1-1h3.5a1 1 0 0 1 1 1c0 1.25.2 2.45.6 3.6a1 1 0 0 1-.25 1z"/></svg>
      </li>
      <li>sales@brightvaleholdingsllc.example
        <svg class="contact-icon" viewBox="0 0 24 24"><path d="M2 5h20v14H2z M2 5l10 8 10-8" fill="var(--green)" stroke="var(--white)" stroke-width="1.5"/></svg>
      </li>
    </ul>

    <span class="edge-mark-green"></span>
    <div class="person">
      <div class="person-name">Milo Jarvis</div>
      <div class="person-title">Business Development</div>
    </div>
  </section>
</body>
</html>
```